Bookmark Design

We would like to design a book mark with logos of our two business and a quote.

One side with the quote "The first wealth is health" - Tobias Quill Harrow and the two logos.

The back side has the two logos with its respective phone numbers and a common address (this is to be advised to the winner of the project).

```html
<!DOCTYPE html>
<html lang="en">
<head>
<meta charset="utf-8">
<title>Bookmark – Front and Back</title>
<link href="https://fonts.googleapis.com/css2?family=Baloo+2:wght@400;500;700;800&display=swap" rel="stylesheet">
<style>
  :root {
    --leaf-green: #67b567;
    --paper: #ffffff;
    --edge: #dfe2e4;
    --hole: #c9cacc;
    --page: #ffffff;
  }
  * { margin: 0; padding: 0; box-sizing: border-box; }
  html, body {
    width: 1200px; height: 1186px; overflow: hidden;
    background: var(--page);
    font-family: "Baloo 2", system-ui, sans-serif;
  }
  .canvas { position: relative; width: 1200px; height: 1186px; }

  .bookmark {
    position: absolute;
    width: 404px; height: 1124px;
    transform-origin: 0 0;
    transform: scale(0.678);
  }
  .bookmark--front { left: 256px; top: 205px; }
  .bookmark--back  { left: 666px; top: 205px; }
  .bookmark__shape { position: absolute; inset: 0; width: 404px; height: 1124px; }
  .bookmark--back .bookmark__shape { transform: scaleX(-1); }

  .text { position: absolute; line-height: 1; white-space: nowrap; }

  /* quote */
  .quote { color: var(--paper); font-weight: 800; }
  .quote__the    { left: 89px;  top: 276px; font-size: 30px; }
  .quote__first  { left: 38px;  top: 312px; font-size: 44px; font-weight: 700; }
  .quote__wealth { left: 130px; top: 286px; font-size: 78px; }
  .quote__is     { left: 58px;  top: 356px; font-size: 40px; font-weight: 700; }
  .quote__health { left: 94px;  top: 346px; font-size: 78px; }
  .quote__author { left: 65px;  top: 445px; font-size: 22px; font-weight: 700; }

  /* brand stand-ins */
  .brand { font-weight: 700; text-align: center; }
  .brand--green { color: var(--leaf-green); }
  .brand--white { color: var(--paper); }
  .brand-dot {
    position: absolute; border-radius: 50%;
    border: 4px solid var(--paper);
  }
  .brand-dot--green { border-color: var(--leaf-green); }

  .front-brands__dental { left: 50px;  top: 1018px; font-size: 26px; width: 150px; white-space: normal; line-height: 1.05; }
  .front-brands__dot    { left: 254px; top: 983px; width: 66px; height: 66px; }
  .front-brands__clinic { left: 210px; top: 1056px; font-size: 19px; width: 154px; }

  .back-clinic__dot  { left: 150px; top: 276px; width: 104px; height: 104px; }
  .back-clinic__name { left: 0; width: 404px; top: 392px; font-size: 30px; }
  .contact { left: 0; width: 404px; text-align: center; font-size: 19px; font-weight: 500; }
  .contact--white { color: var(--paper); }
  .contact--green { color: var(--leaf-green); }
  .back-clinic__address { top: 474px; }
  .back-clinic__phone   { top: 506px; }

  .back-dental__name    { left: 0; width: 404px; top: 890px; font-size: 40px; }
  .back-dental__address { top: 1025px; }
  .back-dental__phone   { top: 1055px; }
</style>
</head>
<body>
<main class="canvas">

  <section class="bookmark bookmark--front" aria-label="Bookmark front">
    <svg class="bookmark__shape" viewBox="0 0 404 1124" aria-hidden="true">
      <defs>
        <radialGradient id="holeFront" cx="0.45" cy="0.35" r="0.7">
          <stop offset="0" stop-color="#e4e5e6"/>
          <stop offset="1" stop-color="#a9abad"/>
        </radialGradient>
      </defs>
      <path d="M0 0 H212 A192 192 0 0 1 404 192 V1124 H0 Z" fill="var(--paper)" stroke="var(--edge)" stroke-width="2"/>
      <path d="M8 8 H212 A184 184 0 0 1 396 192 V646 H200 C110 646 38 700 8 786 Z" fill="var(--leaf-green)"/>
      <circle cx="61" cy="59" r="30" fill="url(#holeFront)" stroke="var(--paper)" stroke-width="5"/>
    </svg>

    <span class="text quote quote__the">"The</span>
    <span class="text quote quote__first">first</span>
    <span class="text quote quote__wealth">wealth</span>
    <span class="text quote quote__is">is</span>
    <span class="text quote quote__health">health"</span>
    <span class="text quote quote__author">- Tobias Quill Harrow</span>

    <span class="text brand brand--green front-brands__dental">Harbour Dental</span>
    <span class="brand-dot brand-dot--green front-brands__dot"></span>
    <span class="text brand brand--green front-brands__clinic">LARKFIELD CLINIC</span>
  </section>

  <section class="bookmark bookmark--back" aria-label="Bookmark back">
    <svg class="bookmark__shape" viewBox="0 0 404 1124" aria-hidden="true">
      <defs>
        <radialGradient id="holeBack" cx="0.55" cy="0.35" r="0.7">
          <stop offset="0" stop-color="#e4e5e6"/>
          <stop offset="1" stop-color="#a9abad"/>
        </radialGradient>
      </defs>
      <path d="M0 0 H212 A192 192 0 0 1 404 192 V1124 H0 Z" fill="var(--paper)" stroke="var(--edge)" stroke-width="2"/>
      <path d="M8 8 H212 A184 184 0 0 1 396 192 V646 H200 C110 646 38 700 8 786 Z" fill="var(--leaf-green)"/>
      <circle cx="61" cy="59" r="30" fill="url(#holeBack)" stroke="var(--paper)" stroke-width="5"/>
    </svg>

    <span class="brand-dot back-clinic__dot"></span>
    <span class="text brand brand--white back-clinic__name">LARKFIELD CLINIC</span>
    <span class="text contact contact--white back-clinic__address">12B Wattle Lane, Brindlewood VIC 3999</span>
    <span class="text contact contact--white back-clinic__phone">+61 3 9000 4821</span>

    <span class="text brand brand--green back-dental__name">Harbour Dental</span>
    <span class="text contact contact--green back-dental__address">12B Wattle Lane, Brindlewood VIC 3999</span>
    <span class="text contact contact--green back-dental__phone">+61 3 9000 4821</span>
  </section>

</main>
</body>
</html>
```